Blow Dry Bar Business Cards

These cards must be eye catching and modern.
You must be willing to work fast and make changes.

Winner will be offered other projects

Files 1 THIS IS THE STYLE CARDS I AM INTRESTED IN!!!
Please be creative, I am paying for my own eye catching design. I need files to be quilla press ready.

COLORS THAT ARE PAINTED INSIDE MY SHOP:
- - - http://www.brennacoat.example/en/explore-colors/painter/color-selector.html?colors=4007-3C

- - - http://www.marlowtint.example/color/paint-colors/quiet-harbor-d58-2

I want the business cards sleek and modern if you use the logo please correct imperfections. I added the part that says Blow Dry Bar (see website).
Do not be afraid to separate the blow dryer from the name to make the cards look like the file with the pink elephant.

SHOULD INCLUDE
*Blow Dryer (we are a blow dry bar not a salon we do not cut or color so do not include sheers of any kind)
*BUSINESS NAME: Simply Swept Up - Blow Dry Bar (PLEASE SEE MY WEBSITE)
* Website: SIMPLYSWEPTUP.EXAMPLE
*Phone number (555) 314-7720
Updates

Quilla press said it can be submitted in JPG

http://www.marlowtint.example/color/paint-colors/quiet-harbor-d58-2 http://www.brennacoat.example/en/explore-colors/painter/color-selector.html?colors=4007-3C ^^^^ These links will take you to the color paint that is painted inside my shop.

Target Market(s)

AGES 18 - 55 WOMEN
HIGH END MARKET

Industry/Entity Type

Salon

Requirements
Must have
• SEE COLOR EXAMPLE FILE
BLOW DRYER
UNIQUE
I LIKE THE CARD WITH THE PINK ELEPHANT THE BEST
Nice to have
• BE AS CREATIVE AND MODERN AS POSSIBLE DO NOT COPY ANY OF THE CARDS BELOW.
Should not have
• SCISSORS
PINK

```html
<!DOCTYPE html>
<html lang="en">
<head>
<meta charset="utf-8">
<title>Simply Swept Up – Business Cards</title>
<link rel="stylesheet" href="https://fonts.googleapis.com/css2?family=Arvo&family=Quicksand:wght@400;500&display=swap">
<style>
  :root {
    --backdrop: #efefef;
    --card: #3b3a43;
    --ink-light: #f4f4f4;
    --accent-dark: #141418;
  }
  html, body {
    margin: 0;
    padding: 0;
    width: 1200px;
    height: 1200px;
    overflow: hidden;
    background: var(--backdrop);
  }
  .canvas {
    position: relative;
    width: 1200px;
    height: 1200px;
  }
  .card {
    position: absolute;
    left: 258px;
    width: 684px;
    height: 384px;
    background: var(--card);
    color: var(--ink-light);
  }
  .card--front { top: 172px; }
  .card--back  { top: 628px; }

  /* Front */
  .brand {
    position: absolute;
    left: 166px;
    top: 312px;
  }
  .brand__name {
    position: absolute;
    left: 162px;
    top: 136px;
    margin: 0;
    font-family: "Arvo", Georgia, serif;
    font-weight: 400;
    font-size: 54px;
    line-height: 1;
    letter-spacing: 0.5px;
    color: var(--ink-light);
    white-space: nowrap;
  }
  .brand__mark {
    position: absolute;
    left: 508px;
    top: 130px;
  }
  .brand__tagline {
    position: absolute;
    left: 254px;
    top: 204px;
    margin: 0;
    font-family: "Quicksand", Arial, sans-serif;
    font-weight: 500;
    font-size: 22px;
    line-height: 1;
    letter-spacing: 0.5px;
    color: var(--ink-light);
    white-space: nowrap;
  }

  /* Back */
  .signature {
    position: absolute;
    left: 84px;
    top: 306px;
    font-family: "Quicksand", Arial, sans-serif;
    text-align: right;
  }
  .signature__name {
    display: block;
    font-weight: 500;
    font-size: 18px;
    line-height: 22px;
    white-space: nowrap;
  }
  .signature__sub {
    display: block;
    font-size: 16px;
    line-height: 20px;
    white-space: nowrap;
  }
  .signature__mark {
    position: absolute;
    left: 306px;
    top: 310px;
  }
  .contact {
    position: absolute;
    left: 424px;
    top: 306px;
    font-family: "Quicksand", Arial, sans-serif;
    font-weight: 500;
    font-size: 16px;
    line-height: 21px;
    letter-spacing: 0.3px;
    white-space: nowrap;
  }
  .contact p { margin: 0; }
</style>
</head>
<body>
<main class="canvas">

  <section class="card card--front" aria-label="Card front">
    <h1 class="brand__name">Swept Up</h1>
    <svg class="brand__mark" width="44" height="44" viewBox="0 0 44 44" aria-hidden="true">
      <circle cx="22" cy="22" r="21" fill="var(--accent-dark)"/>
    </svg>
    <p class="brand__tagline">premier blow dry bar</p>
  </section>

  <section class="card card--back" aria-label="Card back">
    <div class="signature">
      <span class="signature__name">Simply Swept Up</span>
      <span class="signature__sub">blow dry bar</span>
    </div>
    <svg class="signature__mark" width="26" height="26" viewBox="0 0 26 26" aria-hidden="true">
      <circle cx="13" cy="13" r="12" fill="var(--accent-dark)"/>
    </svg>
    <div class="contact">
      <p class="contact__web">SIMPLYSWEPTUP.EXAMPLE</p>
      <p class="contact__phone">P: (555) 314-7720</p>
    </div>
  </section>

</main>
</body>
</html>
```